Geschäftspapiere für unternehmerische Holding für Beteiligungen, Projektgesellschaften und kaufmännische Steuerung
Zielgruppe
Die Hollwen GmbH ist eine unternehmerische Holding für Beteiligungen, Projektgesellschaften und kaufmännische Steuerung. Sie übernimmt Management-, Controlling- und Strukturierungsaufgaben für verbundene Unternehmen.
Zielgruppe sind Banken, Investoren, Geschäftspartner, Steuerberater, Rechtsanwälte, Behörden sowie Geschäftsführungen und Gesellschafter von Beteiligungs- und Projektgesellschaften.
Aufgabenstellung
Gesucht wird ein digitales Briefpapier für die Hollwen GmbH, das sowohl als PDF/Dokumentvorlage als auch beim Ausdruck professionell funktioniert.
Wichtig ist ein sehr klarer, hochwertiger und seriöser Auftritt. Das Design soll reduziert, strukturiert und geschäftlich wirken – keine verspielten Elemente, keine überladenen Grafiken, keine auffälligen Muster.
Das Briefpapier muss drucktauglich sein. Bitte ausreichende Druckränder und Sicherheitsabstände berücksichtigen, damit Kopf- und Fußbereich auch auf normalen Büro- und Laserdruckern sauber ausgegeben werden können. Das Layout soll sowohl digital als auch gedruckt stimmig aussehen.
Format: DIN A4 Hochformat.
Gewünschte Inhalte:
* Logo der Hollwen GmbH
* Firmenname: Hollwen GmbH
* Geschäftsanschrift: Lindauer Weg 52, 80339 München
* Telefon: 089 58210946
* E-Mail: info@hollwenbeta.example
* Webseite: hollwenbeta.example
* Geschäftsführung: Dipl.-Wirtschaftsing. (FH) Till Osterwald
* Registergericht / Amtsgericht München HRB 527081
* Bankverbindung IBAN DE918204 5571 0009 1826 40
Besonderer Wert liegt auf:
* hochwertiger Holding-/Investment-Anmutung
* sehr guter Lesbarkeit
* klarer Kopf- und Fußzeile
* sauberer Typografie
* professioneller Nutzbarkeit für Angebote, Verträge, Behörden- und Bankkorrespondenz
Bitte das Design so anlegen, dass es später als editierbare Word-/PDF-Vorlage genutzt werden kann und sowohl das Logo, als auch die Farben entsprechend verwenden.

```html
<!DOCTYPE html>
<html lang="de">
<head>
<meta charset="utf-8">
<title>Hollwen GmbH – Briefpapier</title>
<link href="https://fonts.googleapis.com/css2?family=Montserrat:wght@300;400;500;600;700&display=swap" rel="stylesheet">
<style>
  :root{
    --navy:#121b33;
    --silver:#c4c8d1;
    --text:#1d2335;
    --muted:#5b6172;
    --paper:#ffffff;
    --backdrop:#ebebeb;
    --rule:#b9bcc4;
  }
  *{box-sizing:border-box;margin:0;padding:0}
  html,body{width:1200px;height:960px;overflow:hidden}
  body{background:var(--backdrop);font-family:"Montserrat",sans-serif;color:var(--text)}
  .sheet{
    position:absolute;left:282px;top:30px;width:636px;height:900px;
    background:var(--paper);box-shadow:0 2px 14px rgba(0,0,0,.12);
  }
  .header-panel{
    position:absolute;left:380px;top:0;width:180px;height:262px;
    background:var(--navy);color:#fff;padding:44px 20px 0 22px;overflow:hidden;
  }
  .brand{
    font-weight:300;font-size:17px;letter-spacing:2.5px;color:var(--silver);
    display:flex;align-items:center;gap:7px;white-space:nowrap;
  }
  .brand-dot{width:6px;height:6px;border-radius:50%;background:var(--silver);flex:none}
  .panel-address{margin-top:34px;font-size:7.6px;line-height:1.55;color:#d9dce3;font-weight:300}
  .panel-address strong{font-weight:600;color:#fff}
  .panel-contacts{list-style:none;margin-top:12px;font-size:7.4px;line-height:1.9;color:#d9dce3;font-weight:300}
  .panel-contacts li{display:flex;align-items:center;gap:7px;white-space:nowrap}
  .panel-contacts svg{width:8px;height:8px;flex:none}
  .sender-line{position:absolute;left:82px;top:212px;font-size:6.8px;color:var(--muted)}
  .sender-line strong{color:var(--navy);font-weight:700}
  .fold-mark{position:absolute;left:20px;width:9px;height:1px;background:var(--rule)}
  .letter{position:absolute;left:82px;top:322px;width:470px;font-size:9px;line-height:1.6}
  .letter p{margin-bottom:10px}
  .salutation{margin-bottom:14px!important}
  .closing{margin-top:44px}
  .signature{display:block;width:118px;height:34px;margin-top:6px;border-radius:3px;
    background:linear-gradient(90deg,#e4e6ec,#f3f4f7)}
  .footer-brand{
    position:absolute;right:40px;top:712px;width:150px;height:54px;background:var(--navy);
    display:flex;align-items:center;justify-content:center;
  }
  .footer-brand .brand{font-size:16px;letter-spacing:3px}
  .footer-info{position:absolute;left:82px;right:40px;top:810px;display:flex;align-items:flex-start;font-size:7.6px;line-height:1.6;color:var(--muted)}
  .footer-info h3{font-size:7.6px;font-weight:700;color:var(--navy)}
  .footer-col{padding-right:22px}
  .footer-divider{width:1px;height:46px;background:var(--navy);margin:0 22px 0 0}
</style>
</head>
<body>
<div class="sheet">
  <header class="header-panel">
    <div class="brand"><span class="brand-dot"></span>HOLLWEN</div>
    <div class="panel-address">
      <strong>Hollwen GmbH</strong><br>
      Lindauer Weg 52<br>
      80339 München
    </div>
    <ul class="panel-contacts">
      <li><svg viewBox="0 0 10 10" fill="none" stroke="#d9dce3" stroke-width="1"><path d="M2 1h2l1 2.5-1.3.8a5 5 0 0 0 2 2l.8-1.3L9 6v2a1 1 0 0 1-1 1A7 7 0 0 1 1 2a1 1 0 0 1 1-1z"/></svg>089 58210946</li>
      <li><svg viewBox="0 0 10 10" fill="none" stroke="#d9dce3" stroke-width="1"><rect x="1" y="2" width="8" height="6"/><path d="M1 2l4 3.5L9 2"/></svg>info@hollwenbeta.example</li>
      <li><svg viewBox="0 0 10 10" fill="none" stroke="#d9dce3" stroke-width="1"><circle cx="5" cy="5" r="4"/><path d="M1 5h8M5 1c-2 2.5-2 5.5 0 8M5 1c2 2.5 2 5.5 0 8"/></svg>www.hollwenbeta.example</li>
    </ul>
  </header>

  <div class="sender-line"><strong>Hollwen GmbH</strong> | Lindauer Weg 52 | 80339 München</div>

  <span class="fold-mark" style="top:297px"></span>
  <span class="fold-mark" style="top:450px"></span>
  <span class="fold-mark" style="top:636px"></span>

  <main class="letter">
    <p class="salutation">Sehr geehrte Damen und Herren,</p>
    <p>Blindtexte nennt man Texte, die bei der Produktion von Publikationen oder Webseiten als Platzhalter für spätere Inhalte stehen, wenn der eigentliche Text noch nicht vorhanden ist. Sie werden auch als Dummy-, Füll- oder Platzhaltertexte bezeichnet. Mitunter sollen Komponisten von Liedern Blindtexte beim Kom- ponieren von Melodien benutzen und diese vor dem Dichten des Liedtextes singen.</p>
    <p>Blindtexte nennt man Texte, die bei der Produktion von Publikationen oder Webseiten als Platzhalter für spätere Inhalte stehen, wenn der eigentliche Text noch nicht vorhanden ist. Sie werden auch als Dummy-, Füll- oder Platzhaltertexte bezeichnet.</p>
    <p class="closing">Mit freundlichen Grüßen</p>
    <span class="signature" role="img" aria-label="Handschriftliche Unterschrift"></span>
  </main>

  <div class="footer-brand"><div class="brand">HOLLWEN</div></div>

  <footer class="footer-info">
    <div class="footer-col">
      <h3>Bankverbindung:</h3>
      Amtsgericht München HRB 527081<br>
      IBAN DE918204 5571 0009 1826 40
    </div>
    <span class="footer-divider"></span>
    <div class="footer-col">
      <h3>Geschäftsführung:</h3>
      Dipl.-Wirtschaftsing. (FH)<br>
      Till Osterwald
    </div>
  </footer>
</div>
</body>
</html>
```